Psychometric Assessment Flyer/Brochure Makeover

TORVEN Consulting is an organisational psychology and human resource management consulting firm based in Melbourne, Australia (www.torvenadvise.com.au). We offer a range of organisational development and executive recruitment services, however the largest part of our business is our online psychometric assessments portal, which is currently used by hundreds of organisations Australia wide as part of their recruitment process.

We are seeking assistance with the redevelopment of an existing 2-page (1 x A4 page double sided) brochure/flyer to make it more impactful. The main purpose of the brochure is to increase sales revenue in our assessments area. We believe that part of the path to increasing/generating revenue is going to be caused by enquiries made to the business as a result of reading this flyer.

Due to the complex nature of psychometric assessments, the content in this existing brochure attached needs to be simplified and easy to understand. Our target audience are businesses and organisations from a range of sectors (eg. not-for-profit/commercial/local & state government). Feel free if you just want to capture key points also.

Please note, we are not just seeking an aesthetic improvement to the brochure, we are seeking direction on the layout and content also.

Target Market(s)

HR Managers, Recruiters, CEO, General Manager, Mangers of private and not for profit organisations.

Font styles to use
Sans Serif

Requirements
Must have
• Company logo (attached); colours are Dark Blue: R53 G67 B113, White: R255 G255 B 255. TORVEN Consulting also uses the following colours for corporate branding and communications:
• Dark Blue: R53 G67 B113 = Hex #354371
• Pink: R202 G48 B146 = Hex #CA3092
• Medium Blue: R80 G145 B205 = Hex #5091CD
• Yellow: R231, G166, B20 = Hex #E7A614
• Contact details as specified in attached flyer.

```html
<!DOCTYPE html>
<html lang="en">
<head>
<meta charset="utf-8">
<title>TORVEN Consulting – Psychometric Assessments Flyer</title>
<link rel="stylesheet" href="https://fonts.googleapis.com/css2?family=Oswald:wght@500;700&family=Lato:wght@400;700&family=Roboto+Condensed:wght@300;400&display=swap">
<style>
:root{
  --navy:#0e1c30;
  --navy-text:#142640;
  --blue:#4f8fd1;
  --blue-light:#7db4e6;
  --pink:#c8308f;
  --pink-light:#e06bb0;
  --grey-head:#8d8f91;
  --cell:#eeeeee;
  --text:#333;
  --muted:#6e6e6e;
  --stage:#c9c9c9;
  --white:#fff;
}
*{box-sizing:border-box;margin:0;padding:0}
html,body{width:1200px;height:1200px;overflow:hidden}
body{background:var(--stage);font-family:"Lato",sans-serif;color:var(--text);position:relative}
.page{position:absolute;top:204px;width:560px;height:792px;background:var(--white);overflow:hidden}
.page--front{left:25px}
.page--back{left:615px}
.abs{position:absolute}
.header-bg{position:absolute;left:0;top:0}
.brand{position:absolute;left:24px;color:var(--white);font-family:"Oswald",sans-serif;font-weight:700;line-height:1}
.brand__name{font-size:40px;letter-spacing:1px}
.brand__sub{font-size:8.5px;letter-spacing:7.2px;margin-top:4px;padding-left:2px}
.header-title{position:absolute;font-family:"Oswald",sans-serif;font-weight:700;color:var(--white);font-size:24px;letter-spacing:.3px}
.center{text-align:center;left:0;right:0}
.h-main{font-family:"Oswald",sans-serif;font-weight:700;color:var(--blue);font-size:25px;letter-spacing:.2px}
.h-main .dark{color:var(--navy-text)}
.lede{font-size:8.4px;line-height:1.35;color:var(--text);padding:0 16px}
.accent{font-family:"Lato",sans-serif;font-weight:700;color:var(--pink);font-size:12.5px;line-height:1.3}
.bullets{list-style:none}
.bullets li{position:relative;padding-left:13px;font-size:8.4px;line-height:1.3}
.bullets li::before{content:"";position:absolute;left:0;top:3px;width:5px;height:5px;background:var(--pink)}
.benefits li{margin-bottom:9px;color:#3a3a3a}
.illustration{position:absolute;left:412px;top:326px;width:100px;height:98px;border-radius:10px;background:radial-gradient(circle at 50% 55%,#5a9ad8 0%,#a8cdee 55%,#fff 80%)}
.bar{position:absolute;left:15px;right:15px;top:440px;height:24px;background:var(--blue);color:var(--white);font-family:"Oswald",sans-serif;font-weight:700;font-size:14px;text-align:center;line-height:24px}
.assess-table{position:absolute;left:15px;right:15px;top:518px;display:grid;grid-template-columns:repeat(3,1fr);gap:0 3px}
.assess-table .th{background:var(--grey-head);color:var(--white);font-size:8.4px;text-align:center;height:14px;line-height:14px;margin:4px 3px 0}
.assess-table .td{background:linear-gradient(#f7f7f7,#e6e6e6);font-size:8.4px;color:#555;text-align:center;height:24px;line-height:24px}
.assess-table .wrap{background:#f0f0f0;padding-bottom:0}
.rule-title{position:absolute;left:15px;right:15px;top:617px;display:flex;align-items:center;gap:10px;font-family:"Oswald",sans-serif;font-weight:700;font-size:15px;color:var(--navy-text)}
.rule-title::before,.rule-title::after{content:"";flex:1;height:1px;background:var(--navy-text)}
.rule-title span{color:var(--blue)}
.diff{position:absolute;left:75px;top:702px;display:flex;gap:16px}
.diff .bullets li{color:#888;font-size:8.2px}
.diff .divider{width:1px;background:#999;height:56px}
.band-bottom{position:absolute;left:0;right:0;bottom:0;height:10px;background:var(--pink)}
.url{position:absolute;left:200px;right:0;top:64px;height:36px;line-height:36px;text-align:center;color:var(--white);font-weight:700;font-size:19px}
.q{position:absolute;left:21px;right:18px}
.q h2{font-family:"Roboto Condensed",sans-serif;font-weight:400;color:var(--blue);font-size:16px;margin-bottom:4px}
.q p{font-size:8px;line-height:1.35;color:#555}
.quote{position:absolute;left:20px;right:30px;top:304px;font-size:11.2px;line-height:1.5;color:#444;padding-left:20px}
.quote .mark{color:var(--pink);font-family:"Oswald",sans-serif;font-weight:700;font-size:20px;line-height:0}
.quote .open{position:absolute;left:0;top:12px}
.results{position:absolute;left:21px;right:18px;top:388px}
.results li{font-size:8.2px;color:#555;line-height:1.6;margin-bottom:5px}
.results li::before{top:4px}
.footer{position:absolute;left:0;top:712px;width:560px;height:70px}
.footer__cta{position:absolute;left:33px;top:11px;color:var(--white);font-family:"Roboto Condensed",sans-serif;font-weight:400;font-size:19px;line-height:1.15}
.footer__phone{position:absolute;left:340px;top:8px;color:var(--white);font-family:"Oswald",sans-serif;font-weight:700;font-size:31px;line-height:1.1}
.footer__email{position:absolute;left:342px;top:47px;color:var(--white);font-size:11px;font-weight:700}
</style>
</head>
<body>

<section class="page page--front">
  <svg class="header-bg" width="560" height="84" viewBox="0 0 560 84" aria-hidden="true">
    <defs><linearGradient id="hdrBlue" x1="0" x2="1"><stop offset="0" stop-color="#4e8ad0"/><stop offset="0.6" stop-color="#7fb6e6"/><stop offset="1" stop-color="#5f9ad6"/></linearGradient></defs>
    <polygon points="0,0 226,0 184,84 0,84" fill="#0e1c30"/>
    <polygon points="232,0 560,0 560,84 190,84" fill="url(#hdrBlue)"/>
  </svg>
  <div class="brand" style="top:18px"><div class="brand__name">TORVEN</div><div class="brand__sub">CONSULTING</div></div>
  <div class="header-title" style="left:223px;top:24px">PSYCHOMETRIC ASSESSMENTS</div>

  <h1 class="abs center h-main" style="top:116px;text-align:center">REDUCE HIRING MISTAKES</h1>
  <p class="abs center lede" style="top:156px;text-align:center">Psychometric Assessments are a powerful and cost-effective way of accurately predicting the likelihood of success of a candidate in any given role. In comparison to traditional recruitment and selection processes such as interviews and reference checking, Psychometric Assessment is evidence based, unbiased and incredibly accurate.</p>
  <p class="abs center accent" style="top:210px;text-align:center">THE MOST ACCURATE PREDICTOR OF<br>ON THE JOB SUCCESS.</p>

  <h2 class="abs center h-main" style="top:258px;text-align:center"><span class="dark">BENEFITS OF</span> ASSESSMENT</h2>
  <p class="abs center lede" style="top:297px;text-align:center">The use of Psychometric Assessments in a recruitment process has led to substantial and sustained work outcomes including:</p>

  <ul class="bullets benefits abs" style="left:21px;top:320px;width:170px">
    <li>Increased productivity and speed to productivity</li>
    <li>Less negative behaviours in the workplace</li>
    <li style="margin-top:17px">Improved employee engagement</li>
    <li style="margin-top:14px">Less disciplinary action required</li>
  </ul>
  <ul class="bullets benefits abs" style="left:208px;top:323px;width:170px">
    <li>Lower turnover</li>
    <li>Less time invested recruiting and training new employees</li>
    <li>Less money spent on advertising vacancies</li>
    <li>Higher client satisfaction ratings</li>
  </ul>
  <div class="illustration" role="img" aria-label="Illustration of a figure juggling icons for hiring, charts and people"></div>

  <div class="bar">WHAT ASSESSMENTS CAN I ADMINISTER?</div>
  <p class="abs center lede" style="top:474px;text-align:center;padding:0 50px">TORVEN offers a range of psychometric assessments designed to measure the likelihood of success at work, as well as potential risk areas. These include:</p>

  <div class="assess-table">
    <div class="wrap"><div class="th">PERSONALITY</div></div>
    <div class="wrap"><div class="th">VALUES</div></div>
    <div class="wrap"><div class="th">COGNITIVE ABILITY</div></div>
    <div class="td">Emotional Intelligence</div>
    <div class="td">Resilience</div>
    <div class="td">Attitudes Toward Diversity</div>
    <div class="td">Engagement</div>
    <div class="td">OH&amp;S</div>
    <div class="td">Counter-Productive Work Behaviours</div>
  </div>

  <div class="rule-title">THE TORVEN&nbsp;<span>DIFFERENCE</span></div>
  <p class="abs center lede" style="top:654px;text-align:center">TORVEN partners with Harbourline University to develop assessments and ensure we are offering the most contemporary measures. Our assessments are evidence-based and designed for recruitment and development purposes, offering benefits such as:</p>

  <div class="diff">
    <ul class="bullets" style="width:200px">
      <li>Risk ratings and knock out factors to help rule candidates in or out</li>
      <li>Simplified and easy to understand reports</li>
      <li>Self-administration through our easy-to-use portal</li>
    </ul>
    <div class="divider"></div>
    <ul class="bullets" style="width:180px">
      <li style="margin-bottom:3px">Pay as You Go – No bulk credits to buy</li>
      <li style="margin-bottom:3px">Buy quickly and easily online</li>
      <li style="margin-bottom:3px">Discounts for volume purchases</li>
      <li>Report available instantly</li>
    </ul>
  </div>
  <div class="band-bottom"></div>
</section>

<section class="page page--back">
  <svg class="header-bg" width="560" height="100" viewBox="0 0 560 100" aria-hidden="true">
    <defs>
      <linearGradient id="hdrBlue2" x1="0" x2="1"><stop offset="0" stop-color="#4e8ad0"/><stop offset="0.6" stop-color="#7fb6e6"/><stop offset="1" stop-color="#5f9ad6"/></linearGradient>
      <linearGradient id="hdrPink" x1="0" x2="1"><stop offset="0" stop-color="#c8308f"/><stop offset="1" stop-color="#b92a84"/></linearGradient>
    </defs>
    <polygon points="0,0 218,0 170,100 0,100" fill="#0e1c30"/>
    <polygon points="224,0 560,0 560,59 196,59" fill="url(#hdrBlue2)"/>
    <polygon points="193,64 560,64 560,100 176,100" fill="url(#hdrPink)"/>
  </svg>
  <div class="brand" style="top:20px;left:21px"><div class="brand__name">TORVEN</div><div class="brand__sub">CONSULTING</div></div>
  <div class="header-title" style="left:222px;top:12px;font-size:23px">PSYCHOMETRIC ASSESSMENTS</div>
  <div class="url">www.torvenadvise.com.au</div>

  <div class="q" style="top:116px">
    <h2>How do I access Psychometric Assessments?</h2>
    <p>Psychometric Assessments can be easily administered by you through our online portal, or TORVEN can manage the entire process on your behalf. The TORVEN Psychometric Portal is an online platform that allows clients to manage HR and organisational development tasks for all stages of the employment cycle.</p>
  </div>
  <div class="q" style="top:188px">
    <h2>How much do Psychometric Assessments cost?</h2>
    <p>TORVEN offers a range of assessments and bundled assessments, with prices starting under $100 per assessment and even less for volume purchases.</p>
  </div>
  <div class="q" style="top:246px">
    <h2>How can I buy Psychometric Assessments?</h2>
    <p>Call the TORVEN Assessment Team on 1300 555 019 to discuss options and arrange set up.</p>
  </div>

  <blockquote class="quote">
    <span class="mark open">“</span>We recently asked one of our clients to tell us about their experience with the TORVEN Psychometric Assessments and how it has changed their recruitment process. This is what Clare Dunmore, General Manager – Human Resources at Wattlebank Aged Care said. <span class="mark">”</span>
  </blockquote>

  <ul class="bullets results">
    <li>30% decrease in advertising costs and agency fees</li>
    <li>The number of departures in the first year of service has decreased by 54% compared to the average of the six years prior.</li>
    <li>Instances of abandonment of employment in the first year of service have decreased by 61% compared to the same period.</li>
    <li>There have been no cases of permanent employees abandoning their employment in their first year since 2013 as opposed to 12 cases in the six years prior.</li>
    <li>In 2014 -2015, fewer staff than any year prior left with between 1 and 2 years service. Better retention has resulted in fewer employment vacancies over fiscal years 2014-2015 and 2015-2016, which equates to improved continuity of care for residents.</li>
    <li>The number of involuntary terminations in the first year of service has decreased by 83% compared to the six years prior to these changes.</li>
    <li>Since 2013 there has been only one termination due to performance within the first year, as opposed to 20 cases in the six years prior.</li>
    <li>Since July 2014 managers have rated 88% of their new employees as either “excellent” or “very good” after three months of work.</li>
    <li>Of the 46 instances of counselling or disciplinary action from 2013 to date, only six instances involved employees hired during this period. Employees hired since 2013 make up 48% of the current workforce but only 13% of the counselling or disciplinary cases.</li>
  </ul>

  <div class="footer">
    <svg width="560" height="70" viewBox="0 0 560 70" aria-hidden="true">
      <defs>
        <linearGradient id="ftPink" x1="0" x2="1"><stop offset="0" stop-color="#c8308f"/><stop offset="1" stop-color="#e06bb0"/></linearGradient>
        <linearGradient id="ftBlue" x1="0" x2="1"><stop offset="0" stop-color="#4e8ad0"/><stop offset="1" stop-color="#6ea8e0"/></linearGradient>
      </defs>
      <polygon points="0,0 302,0 314,35 302,70 0,70" fill="url(#ftPink)"/>
      <polygon points="310,0 560,0 560,70 310,70 322,35" fill="url(#ftBlue)"/>
    </svg>
    <div class="footer__cta">For further information please<br>contact the Assessments Team:</div>
    <div class="footer__phone">1300 555 019</div>
    <div class="footer__email">assessments@torvenadvise.com.au</div>
  </div>
</section>

</body>
</html>
```